Information Technology Company needs a Website...

We need a single page website for new technology company called:

MERIDEL FALLS TECHNOLOGY GROUP
Based in Ojai CA.

We are offering three primary services:

- Business Solutions

- IT Services

- Software Implementation and Consulting

We want a single page design where all content scrolls down/up on one page. We're looking for the following characteristics:

- Home/Landing
- Active background with panoramic view (Will provide content)

- Business Solutions, IT Services, Software Implementation and Consulting

List of software vendors we recommend (Company logos)

- About
- History
- Our Team
- Partners

I'll upload our new logo as soon as we get the design files. I'll also send over some example website layout's that we like shortly.

Target Market(s)

Small/Medium Businesses

Industry/Entity Type

Information Technology

Number of Pages Required

1 page

Font styles to use
Other font styles liked:
• Sansation

Requirements
Must have
• Full page browser width, easy navigation and visibility. Creative design, not like every other "Technology" website template. Should be the "One Page" design where each section is below the next and the user scrolls down the page through the whole site. I like the concept of the following website in the main "Whiteboard" image:
• http://www.plavorix.com/design/4829137
• And the way this site does the active panoramic background:
• http://www.kelbrantworks.com/
• Something interesting and appealing to potential clients looking for Small/Medium business solutions and IT Services.
• Use uploaded Logo to establish color and theme for website.
Should not have
• Look the same as every other information technology website template.

```html
<!DOCTYPE html>
<html lang="en">
<head>
<meta charset="utf-8">
<title>Meridel Falls Technology Group</title>
<link rel="stylesheet" href="https://fonts.googleapis.com/css2?family=Play:wght@400;700&family=Open+Sans:wght@400;600&display=swap">
<style>
:root{
  --orange:#e2421d;
  --orange-dark:#c93713;
  --dark:#3f3f41;
  --dark-2:#4a4a4c;
  --text:#555;
  --light:#f1f1f1;
  --white:#fff;
  --line:#dcdcdc;
  --grey-btn:#4d4d4f;
}
*{box-sizing:border-box;margin:0;padding:0}
html,body{width:1200px;height:2293px;overflow:hidden}
body{
  font-family:"Open Sans",Arial,sans-serif;color:var(--text);
  background:linear-gradient(180deg,#0f2a4a 0%,#1b4c6e 25%,#2d3f55 50%,#7a5a3a 65%,#23324a 80%,#152238 100%);
  position:relative;
}
.city-backdrop{position:absolute;inset:0}
.page{position:absolute;left:107px;top:0;width:966px;height:2293px;background:var(--white)}
.heading{font-family:"Play",Arial,sans-serif;font-weight:700;color:var(--orange);text-transform:uppercase;letter-spacing:.5px}
.btn{display:inline-block;background:var(--orange);color:var(--white);font-size:10px;padding:8px 11px;text-transform:uppercase;line-height:1}

/* top bar */
.topbar{height:34px;background:var(--dark);color:#ddd;font-size:10px;display:flex;align-items:center;padding:0 104px 0 107px;justify-content:space-between}
.topbar .contact{display:flex;gap:18px;align-items:center}
.topbar .contact span{display:flex;align-items:center;gap:6px}
.topbar .social{display:flex;gap:9px}
.topbar .social i{width:8px;height:8px;background:var(--orange);border-radius:50%;display:block}

/* header */
.header{height:101px;display:flex;align-items:center;padding:0 104px 0 104px;justify-content:space-between;box-shadow:0 2px 4px rgba(0,0,0,.12);position:relative;z-index:2}
.brand{font-family:"Play",Arial,sans-serif;font-weight:700;color:var(--dark);line-height:1.05;display:flex;align-items:center;gap:8px}
.brand .mark{width:14px;height:14px;background:var(--orange)}
.brand .name{font-size:22px}
.brand .sub{font-size:11px;letter-spacing:2px}
.nav{display:flex;align-items:center;gap:0}
.nav a{font-size:10px;color:#444;text-transform:uppercase;padding:9px 12px;text-decoration:none}
.nav a.active{background:var(--orange);color:var(--white);padding:9px 15px;margin-right:6px}
.nav .search{width:29px;height:29px;background:var(--orange);margin-left:6px;display:flex;align-items:center;justify-content:center}

/* hero */
.hero{height:350px;position:relative;background:linear-gradient(100deg,#8f9aa6 0%,#cfd6dd 35%,#e9ecef 60%,#b9c3cc 100%)}
.hero .caption{position:absolute;left:0;top:102px;width:468px;height:153px;background:rgba(70,70,72,.72);padding:22px 0 0 104px;color:var(--white)}
.hero .caption h1{font-family:"Play",Arial,sans-serif;font-weight:400;font-size:29px;letter-spacing:1px;margin-bottom:8px}
.hero .caption p{font-size:10px;line-height:16px;width:300px}
.hero .dots{position:absolute;left:471px;top:324px;display:flex;gap:5px}
.hero .dots i{width:7px;height:7px;border-radius:50%;background:#666;display:block}
.hero .dots i:first-child{background:var(--orange)}

/* welcome */
.welcome{height:226px;text-align:center;padding-top:35px}
.welcome h2{font-size:21px;margin-bottom:14px}
.welcome p{font-size:9px;line-height:16px;width:760px;margin:0 auto 27px;color:#555}

/* services */
.services{height:374px;background:var(--light);text-align:center;padding-top:42px;position:relative}
.services h2{font-size:21px;margin-bottom:30px}
.service-grid{display:flex;width:816px;margin:0 auto}
.service{flex:1;padding:6px 18px 0;border-left:1px solid var(--line);height:184px}
.service:first-child{border-left:none}
.service svg{height:52px;width:56px;margin-bottom:16px}
.service h3{font-size:16px;line-height:19px;margin-bottom:20px;font-family:"Play",Arial,sans-serif;color:var(--orange);text-transform:uppercase}
.service p{font-size:9px;line-height:15px;color:#555;text-align:justify;text-align-last:center}
.services .btn{margin-top:-4px}

/* history */
.history{height:375px;display:flex}
.history .panel{width:483px;background:var(--orange);color:var(--white);padding:66px 40px 0 107px}
.history h2{font-family:"Play",Arial,sans-serif;font-size:20px;font-weight:400;letter-spacing:1px;margin-bottom:18px}
.history p{font-size:8.5px;line-height:15px;margin-bottom:14px}
.history .btn{background:var(--grey-btn);margin-top:6px;padding:10px 11px}
.history .photo{flex:1;background:linear-gradient(135deg,#c9ccd0 0%,#e7d2b0 40%,#d9b986 60%,#5a6e85 100%)}

/* team */
.team{height:393px;text-align:center;padding-top:44px;position:relative}
.team h2{font-size:21px;margin-bottom:34px}
.team-row{display:flex;width:816px;margin:0 auto}
.member{flex:1;border-left:1px solid var(--line);padding:0 22px;height:245px}
.member:first-child{border-left:none}
.avatar{width:110px;height:110px;border-radius:50%;margin:0 auto 30px;background:radial-gradient(circle at 50% 40%,#c89a7c,#6b4b3a)}
.member h3{font-family:"Play",Arial,sans-serif;font-size:16px;color:var(--orange);text-transform:uppercase;margin-bottom:16px}
.member p{font-size:9px;line-height:15px;color:#555}
.arrow{position:absolute;width:14px;height:14px}

/* partners */
.partners{height:257px;background:linear-gradient(180deg,#e4e6e9,#eef0f2);text-align:center;padding-top:40px;position:relative}
.partners h2{font-size:21px;margin-bottom:34px}
.partner-row{display:flex;gap:16px;width:759px;margin:0 auto}
.partner{width:139px;height:88px;background:var(--white);border:1px solid #d4d4d4;display:flex;align-items:center;justify-content:center}
.partner i{display:block;width:80px;height:20px;background:#d0d4d8;border-radius:3px}

/* footer */
.footer{height:183px;background:var(--dark-2);color:#ddd;position:relative;padding:28px 104px 0 104px}
.footer h4{font-family:"Play",Arial,sans-serif;font-weight:400;color:var(--white);font-size:15px;letter-spacing:.5px;margin-bottom:10px}
.footer .info{font-size:8.5px;line-height:16px}
.footer .follow{position:absolute;left:729px;top:28px}
.footer .follow .circles{display:flex;gap:7px;margin-top:4px}
.footer .follow .circles i{width:29px;height:29px;border-radius:50%;background:#8b8b8d;display:block}
.footer .follow .circles i:first-child{background:var(--orange)}
.footer .bottom{position:absolute;left:104px;right:104px;top:142px;display:flex;justify-content:space-between;font-size:8.5px;text-transform:uppercase;color:#ddd}
</style>
</head>
<body>
<div class="city-backdrop" role="img" aria-label="Panoramic night view of a city skyline with illuminated towers"></div>

<div class="page">
  <div class="topbar">
    <div class="contact">
      <span><svg width="9" height="9" viewBox="0 0 10 10"><path d="M2 1l2 2-1 1.5c.7 1.3 1.2 1.8 2.5 2.5L7 6l2 2-1.5 1.5C4 9 1 6 .5 2.5z" fill="#e2421d"/></svg>5550-142-7730</span>
      <span><svg width="10" height="8" viewBox="0 0 10 8"><rect x=".5" y=".5" width="9" height="7" fill="none" stroke="#e2421d"/><path d="M.5 .5l4.5 4 4.5-4" fill="none" stroke="#e2421d"/></svg>INFO@MERIDELFALLS.COM</span>
    </div>
    <div class="social"><i></i><i></i><i></i><i></i></div>
  </div>

  <header class="header">
    <div class="brand"><span class="mark"></span><div><div class="name">MERIDEL FALLS</div><div class="sub">TECHNOLOGY GROUP</div></div></div>
    <nav class="nav">
      <a class="active">Home</a><a>About</a><a>Services</a><a>History</a><a>Our Team</a><a>Partners</a><a>Contact Us</a>
      <span class="search"><svg width="12" height="12" viewBox="0 0 12 12"><circle cx="5" cy="5" r="3.5" fill="none" stroke="#fff" stroke-width="1.6"/><path d="M7.5 7.5L11 11" stroke="#fff" stroke-width="1.8"/></svg></span>
    </nav>
  </header>

  <section class="hero" role="img" aria-label="Business team meeting around a table in a bright office">
    <div class="caption">
      <h1>BUSINESS SOLUTIONS</h1>
      <p>Create extraordinary outcomes with our clients by delivering solutions based on highly skilled and professional talent.</p>
    </div>
    <div class="dots"><i></i><i></i><i></i></div>
  </section>

  <section class="welcome">
    <h2 class="heading">Welcome to Meridel Falls Consulting</h2>
    <p>Kelbrant Corp. (NYSE: KLB) seeks to create extraordinary outcomes with our clients by delivering solutions based on highly skilled and professional talent. Our client offerings include an array of engineering design project solutions, information technology project solutions and managed services, specialty technology staff augmentation, and program and managed staffing services. Our clients are corporations in multiple industries.</p>
    <span class="btn">Read More</span>
  </section>

  <section class="services">
    <h2 class="heading">Our Services</h2>
    <div class="service-grid">
      <div class="service">
        <svg viewBox="0 0 56 52"><circle cx="28" cy="10" r="7" fill="none" stroke="#e2421d" stroke-width="3"/><rect x="25" y="17" width="6" height="4" fill="#e2421d"/><circle cx="28" cy="30" r="7" fill="#e2421d"/><path d="M12 52c0-10 7-15 16-15s16 5 16 15z" fill="#e2421d"/></svg>
        <h3>Business<br>Solutions</h3>
        <p>Kelbrant Corp. (NYSE: KLB) seeks to create extraordinary outcomes with our clients</p>
      </div>
      <div class="service">
        <svg viewBox="0 0 56 52"><rect x="4" y="4" width="36" height="28" fill="#e2421d"/><rect x="8" y="8" width="28" height="20" fill="#fff"/><rect x="18" y="32" width="8" height="8" fill="#e2421d"/><rect x="10" y="40" width="24" height="4" fill="#e2421d"/><rect x="43" y="10" width="10" height="34" fill="#e2421d"/></svg>
        <h3>IT<br>Services</h3>
        <p>Kelbrant Corp. (NYSE: KLB) seeks to create extraordinary outcomes with our clients</p>
      </div>
      <div class="service">
        <svg viewBox="0 0 56 52"><g fill="#e2421d"><circle cx="26" cy="24" r="14"/><rect x="22" y="4" width="8" height="40"/><rect x="6" y="20" width="40" height="8"/><rect x="22" y="4" width="8" height="40" transform="rotate(45 26 24)"/><rect x="22" y="4" width="8" height="40" transform="rotate(-45 26 24)"/></g><circle cx="26" cy="24" r="6" fill="#f1f1f1"/><path d="M32 32l14 14" stroke="#e2421d" stroke-width="5"/></svg>
        <h3>Software<br>Implementation</h3>
        <p>Kelbrant Corp. (NYSE: KLB) seeks to create extraordinary outcomes with our clients</p>
      </div>
      <div class="service">
        <svg viewBox="0 0 56 52"><g fill="#e2421d"><circle cx="14" cy="8" r="5"/><circle cx="42" cy="8" r="5"/><rect x="8" y="15" width="12" height="18"/><rect x="36" y="15" width="12" height="18"/><rect x="20" y="22" width="16" height="6"/><rect x="10" y="36" width="8" height="14"/><rect x="38" y="36" width="8" height="14"/></g></svg>
        <h3>Software<br>Consulting</h3>
        <p>Kelbrant Corp. (NYSE: KLB) seeks to create extraordinary outcomes with our clients</p>
      </div>
    </div>
    <span class="btn">Read More</span>
  </section>

  <section class="history">
    <div class="panel">
      <h2>HISTORY</h2>
      <p>Kelbrant Corp. (NYSE: KLB) seeks to create extraordinary outcomes with our clients by delivering solutions based on highly skilled and professional talent. Our client offerings include an array of engineering</p>
      <p>Kelbrant Corp. (NYSE: KLB) seeks to create extraordinary outcomes with our clients by delivering solutions based on highly skilled and professional talent. Our client offerings include an array of engineering design project solutions, information technology project solutions and managed services, specialty technology staff augmentation, and program and managed staffing services. Our clients are corporations in multiple industries.</p>
      <span class="btn">Read More</span>
    </div>
    <div class="photo" role="img" aria-label="Colleagues working with laptops and a tablet around a wooden table"></div>
  </section>

  <section class="team">
    <h2 class="heading">Our Team</h2>
    <svg class="arrow" style="left:74px;top:222px" viewBox="0 0 14 14"><path d="M9 2L4 7l5 5" fill="none" stroke="#333" stroke-width="1.5"/></svg>
    <svg class="arrow" style="left:872px;top:222px" viewBox="0 0 14 14"><path d="M5 2l5 5-5 5" fill="none" stroke="#333" stroke-width="1.5"/></svg>
    <div class="team-row">
      <div class="member"><div class="avatar" role="img" aria-label="Portrait photo of Dorian Fellowes"></div><h3>Dorian Fellowes</h3><p>Lorem ipsum dolor sit amet, consectetur adipi-scing elit, sed do eiusmod tempor incididunt ut labore et dolore magna aliqua.</p></div>
      <div class="member"><div class="avatar" role="img" aria-label="Portrait photo of Ashlyn Harte"></div><h3>Ashlyn Harte</h3><p>Lorem ipsum dolor sit amet, consectetur adipi-scing elit, sed do eiusmod tempor incididunt ut labore et dolore magna aliqua.</p></div>
      <div class="member"><div class="avatar" role="img" aria-label="Portrait photo of Felipe Torrance"></div><h3>Felipe Torrance</h3><p>Lorem ipsum dolor sit amet, consectetur adipi-scing elit, sed do eiusmod tempor incididunt ut labore et dolore magna aliqua.</p></div>
    </div>
  </section>

  <section class="partners">
    <h2 class="heading">Our Partners</h2>
    <svg class="arrow" style="left:74px;top:147px" viewBox="0 0 14 14"><path d="M9 2L4 7l5 5" fill="none" stroke="#333" stroke-width="1.5"/></svg>
    <svg class="arrow" style="left:872px;top:147px" viewBox="0 0 14 14"><path d="M5 2l5 5-5 5" fill="none" stroke="#333" stroke-width="1.5"/></svg>
    <div class="partner-row">
      <div class="partner"><i></i></div><div class="partner"><i></i></div><div class="partner"><i></i></div><div class="partner"><i></i></div><div class="partner"><i></i></div>
    </div>
  </section>

  <footer class="footer">
    <h4>CONACT US</h4>
    <div class="info">#2868Lorem ipsum dolor sit amet, consectetur adipiscing elit,<br>5550-142-7730<br>info@meridelfalls.com</div>
    <div class="follow"><h4>FOLLOW US</h4><div class="circles"><i></i><i></i><i></i><i></i></div></div>
    <div class="bottom"><span>Home / About / Services / History / Our Team / Partners / Contact Us</span><span>© 2016 Meridel Falls Consulting. All rights reserved.</span></div>
  </footer>
</div>
</body>
</html>
```